IT consulting firm needs brochures for each of our practices

We have a basic draft of a brochure for each of the practices, we offer services as IT consultants and need a better look for each one. We want to use client logos and information on our expertise for each brochure/practice.
Our website has the different areas we serve as reference.

Consulting

```html
<!DOCTYPE html>
<html lang="en">
<head>
<meta charset="utf-8">
<title>Veltrax Oil &amp; Gas Practice Brochure</title>
<link rel="stylesheet" href="https://fonts.googleapis.com/css2?family=Bebas+Neue&family=Open+Sans:wght@400;600;700&family=Roboto+Condensed:wght@700&display=swap">
<style>
  :root {
    --canvas: #ffffff;
    --page: #ffffff;
    --brand-blue: #2b4fa8;
    --brand-navy: #16357f;
    --rule-blue: #3b5cc4;
    --text: #3a3a3a;
    --heading: #222222;
    --teal: #1b8a9e;
    --green: #6aa33c;
    --deep-teal: #0f3a45;
    --button-blue: #2f7bc8;
    --bullet-ring: #49a7e3;
    --bullet-edge: #e8b923;
    --wave-light: #eaf1fb;
    --wave-mid: #cfdff4;
  }
  * { box-sizing: border-box; margin: 0; padding: 0; }
  html, body { width: 1200px; height: 900px; overflow: hidden; background: var(--canvas); }
  body { position: relative; font-family: "Open Sans", Arial, sans-serif; color: var(--text); }

  .page {
    position: absolute;
    background: var(--page);
    box-shadow: 0 6px 18px rgba(0,0,0,0.35);
    overflow: hidden;
  }
  .page--front { left: 38px; top: 48px; width: 530px; height: 727px; }
  .page--back { left: 624px; top: 118px; width: 528px; height: 727px; }

  .page__waves {
    position: absolute; left: 0; top: 0; width: 100%; height: 110px;
    background: linear-gradient(175deg, var(--wave-light) 0%, var(--wave-mid) 35%, rgba(255,255,255,0) 80%);
  }

  .masthead { position: absolute; left: 48px; top: 46px; width: 460px; height: 68px; }
  .masthead__brand {
    position: absolute; left: 0; top: 2px;
    font-family: "Open Sans", Arial, sans-serif; font-weight: 700;
    font-size: 32px; color: var(--brand-blue); letter-spacing: -0.5px; line-height: 42px;
  }
  .masthead__company {
    position: absolute; left: 2px; top: 56px; white-space: nowrap;
    font-size: 8.4px; font-weight: 700; color: var(--brand-navy); line-height: 10px;
  }
  .masthead__title {
    position: absolute; left: 160px; top: 36px; white-space: nowrap;
    font-family: "Bebas Neue", Impact, sans-serif; font-size: 27px; font-weight: 400;
    color: var(--brand-blue); letter-spacing: 0.5px; line-height: 26px;
  }
  .masthead__rule {
    position: absolute; left: 160px; top: 64px; width: 300px; height: 1px; background: var(--rule-blue);
  }

  .photo { position: absolute; }
  .photo--platform {
    left: 48px; top: 125px; width: 435px; height: 135px;
    background: linear-gradient(180deg, #f3a72a 0%, #e8891a 45%, #b85a10 75%, #3a2208 100%);
  }
  .photo--refinery {
    left: 47px; top: 127px; width: 435px; height: 189px;
    background: linear-gradient(180deg, #1e2f66 0%, #2f4a8e 40%, #4a78b8 70%, #2a3a5a 100%);
  }

  .intro {
    position: absolute; left: 48px; top: 269px; width: 438px;
    font-size: 8.1px; line-height: 12.2px; letter-spacing: -0.05px;
  }

  .pillars { position: absolute; left: 48px; top: 323px; width: 436px; height: 100px; }
  .pillar { position: absolute; top: 0; width: 141px; }
  .pillar:nth-child(1) { left: 0; }
  .pillar:nth-child(2) { left: 147px; }
  .pillar:nth-child(3) { left: 296px; width: 140px; }
  .pillar__head {
    height: 29px; display: flex; align-items: center; justify-content: center; text-align: center;
    font-family: "Roboto Condensed", Arial, sans-serif; font-weight: 700; font-size: 7.6px;
    line-height: 9.5px; color: #fff; padding: 0 6px;
  }
  .pillar--teal .pillar__head { background: var(--teal); }
  .pillar--green .pillar__head { background: var(--green); }
  .pillar--deep .pillar__head { background: var(--deep-teal); }
  .pillar__body { margin-top: 7px; font-size: 7.4px; line-height: 10px; }

  .section-heading {
    position: absolute; font-size: 9px; font-weight: 700; color: var(--heading);
    padding-bottom: 3px; border-bottom: 1px solid var(--rule-blue); white-space: nowrap;
  }
  .section-heading--tasks { left: 48px; top: 428px; width: 270px; }
  .section-heading--solutions { left: 48px; top: 333px; padding-right: 6px; font-size: 8.4px; font-weight: 600; }

  .clients-label {
    position: absolute; left: 353px; top: 424px; width: 130px; height: 20px;
    background: var(--button-blue); color: #fff; font-size: 8.6px; font-weight: 600;
    display: flex; align-items: center; justify-content: center;
  }
  .client-list { position: absolute; left: 353px; top: 458px; width: 130px; list-style: none; }
  .client-list li {
    height: 53px; display: flex; align-items: center; justify-content: center;
    font-size: 15px; font-weight: 700; color: var(--brand-navy);
  }

  .bullet-list { position: absolute; list-style: none; }
  .bullet-list li { position: relative; padding-left: 16px; font-size: 7.3px; line-height: 9.6px; }
  .bullet-list li::before {
    content: ""; position: absolute; left: 0; top: 0; width: 10px; height: 10px; border-radius: 50%;
    background: var(--brand-navy); border: 2px solid var(--bullet-ring);
    box-shadow: 0 0 0 1px var(--bullet-edge);
  }
  .bullet-list--tasks { left: 57px; top: 455px; width: 296px; }
  .bullet-list--tasks li { height: 19.3px; }
  .bullet-list--tasks li.tall { height: 25px; }
  .bullet-list--provides { left: 72px; top: 439px; width: 380px; }
  .bullet-list--provides li { height: 22.3px; }

  .lead-copy {
    position: absolute; left: 48px; top: 356px; width: 438px; font-size: 7.8px; line-height: 11.4px;
  }
  .lead-copy strong { font-weight: 700; color: var(--heading); }
  .sub-heading { position: absolute; left: 48px; font-size: 8.4px; font-weight: 700; color: var(--heading); }
  .sub-heading--provides { top: 417px; }
  .sub-heading--commitment { top: 606px; }
  .commitment-copy {
    position: absolute; left: 48px; top: 627px; width: 438px; font-size: 7.8px; line-height: 11.4px;
  }
</style>
</head>
<body>

<section class="page page--front">
  <div class="page__waves"></div>
  <header class="masthead">
    <div class="masthead__brand">Veltrax</div>
    <div class="masthead__company">Veltrax Consulting Services, Inc.</div>
    <h1 class="masthead__title">Veltrax Oil &amp; Gas Practice</h1>
    <div class="masthead__rule"></div>
  </header>

  <div class="photo photo--platform" role="img" aria-label="Offshore oil platform silhouetted against an orange sunset over the sea"></div>

  <p class="intro">In these challenging and rapidly evolving times we have seen stricter environmental regulations and public demands on their operational responsibilities, forcing Oil &amp; Gas companies to manage their risk continously and even attempt to predict the future. With preductive analytic solutions companies are better equiped today than ever before. Our success in providing such solutions to the industryis attibuted to:</p>

  <div class="pillars">
    <div class="pillar pillar--teal">
      <div class="pillar__head">Full adoption of the FI&amp;R analytical diagnosis &amp; modeling methodology</div>
      <p class="pillar__body">This methodology seamlessly aligns engineering and analytical approaches. Full adoption of predictive models and issued predictive alarms and alerts, by the client’s organization (operators and domain service organization).</p>
    </div>
    <div class="pillar pillar--green">
      <div class="pillar__head">Full predictive surveillance service</div>
      <p class="pillar__body">Full predictive surveillance service for multi-vendor equipment and holistic processes, integrated in the daily operational activity.</p>
    </div>
    <div class="pillar pillar--deep">
      <div class="pillar__head">Customer’s acknowledged benefit</div>
      <p class="pillar__body">Elimination of multiple contractual points for niche/product services with many equipment vendors – now one single surveillance system in place</p>
    </div>
  </div>

  <h2 class="section-heading section-heading--tasks">Veltrax helped these clients on the following tasks:</h2>
  <ul class="bullet-list bullet-list--tasks">
    <li>Implementation and operation of collaborative engineering centers of excellence.</li>
    <li>Operational equipment alert monitoring.</li>
    <li class="tall">Analytical Diagnosis with engineering and analytical approach/resources – frequency driven by the Predictive Surveillance input.</li>
    <li>Resulting in discovery of Early Predictive Indicators and Root causes.</li>
    <li>Creation of predictive models.</li>
    <li>Implementation of models and predictive alarms/alerts on a frequent basis.</li>
    <li>Performance gap detection and handling on continuous basis.</li>
    <li>Handling of Prediction of process and facility upsets.</li>
    <li>Adjustment and handling of predictive Alarms/alerts.</li>
    <li>Automatic interpretation – monitoring of performance, handling, adjustment.</li>
    <li>Predictive Surveillance – performance monitoring, adjustments &amp; handling.</li>
  </ul>

  <div class="clients-label">Some of our clients include</div>
  <ul class="client-list">
    <li>Northmere</li>
    <li>Calden</li>
    <li>Ostrel</li>
    <li>Harlow Energy</li>
  </ul>
</section>

<section class="page page--back">
  <div class="page__waves"></div>
  <header class="masthead">
    <div class="masthead__brand">Veltrax</div>
    <div class="masthead__company">Veltrax Consulting Services, Inc.</div>
    <h1 class="masthead__title">Veltrax Oil &amp; Gas Practice</h1>
    <div class="masthead__rule"></div>
  </header>

  <div class="photo photo--refinery" role="img" aria-label="Oil refinery lit up at dusk under a deep blue sky"></div>

  <h2 class="section-heading section-heading--solutions">Veltrax Solutions Include: vX-Support™</h2>
  <p class="lead-copy"><strong>Veltrax vX-Support™</strong> is an internet-driven solution for organizations that, after implementing software solutions, need additional support to maintain their system’s operation. Veltrax offers bundles of consulting hours from its specialized consultants in Data Integration, Data Warehousing Construction, Business Intelligence Reporting and Sophisticated Analysis. All these services are provided at a low cost, with high quality and maximum accessibility.</p>

  <h3 class="sub-heading sub-heading--provides">The solution provides:</h3>
  <ul class="bullet-list bullet-list--provides">
    <li>As needed support to business users</li>
    <li>Intergrated reporting options</li>
    <li>Adjustment of systems to local legal requirements</li>
    <li>IT support for software integration and Training of support staff</li>
    <li>Alert Monitoring</li>
    <li>Risk Management</li>
    <li>Support to your business</li>
  </ul>

  <h3 class="sub-heading sub-heading--commitment">Service Commitment:</h3>
  <p class="commitment-copy">Once an issue concerning the use of software is reported, Veltrax agrees to assign a resource to verify the issue. In critical issues (High), this resource will be assigned within specific pre-determined business hours and for regular issues (Low and Medium), the resource will be assigned within one business day.</p>
</section>

</body>
</html>
```